Website for a service provided by a Canadian Immigration Company

Design and Code a website for a Canadian immigration company which provides service to clients all across the world. the website should be very Canadian centric and have 4-5 pages. Basic, classy modern. I have the logo s already designed. Please contact me and I can send you some more details. It's basically a service which is provided to clients who are below 17 and need a guardian in canada to sign their documents that they will be looked after them. It's called custodianship. You can google the term and you will understand what it means
Updates

didn't realize it was just a day

Target Market(s)

17-55

Industry/Entity Type

Immigration

Coding

Coded - Design and coding required

Number of Pages Required

5+ page

Font styles to use
Sans Serif

Colors
EE7325
F08F49
F5BC92
FAE3D3
FDF4ED
EB3D1F
EC4F4E
F09395
F8D3D4
FCEDEE

Requirements
Must have
• Pages with some graphics, some small animations like clients served, projects completed

```html
<!DOCTYPE html>
<html lang="en">
<head>
<meta charset="utf-8">
<title>guardwell.ca — Study in Canada as a minor</title>
<link href="https://fonts.googleapis.com/css2?family=Montserrat:wght@400;500;600;700&display=swap" rel="stylesheet">
<style>
:root{
  --red:#eb2027;
  --red-soft:#f09395;
  --pink:#f8d3d4;
  --ink:#1f1f1f;
  --dark:#231f20;
  --text:#3a3a3a;
  --muted:#8a8a8a;
  --grey-bg:#f2f2f2;
  --white:#ffffff;
}
*{box-sizing:border-box;margin:0;padding:0}
html,body{width:1200px;height:3190px;overflow:hidden}
body{position:relative;font-family:'Montserrat',sans-serif;color:var(--text);background:var(--white)}
.abs{position:absolute}
.btn{position:absolute;display:flex;align-items:center;justify-content:center;background:var(--red);color:var(--white);
  font-weight:600;font-size:15px;text-decoration:none;clip-path:polygon(0 0,94% 0,100% 100%,6% 100%)}
.mark-sq{display:inline-block;width:14px;height:14px;background:var(--red)}
.brand{position:absolute;display:flex;align-items:center;gap:12px;font-weight:600;font-size:30px;letter-spacing:-.5px}

/* header */
.site-header{position:absolute;left:0;top:0;width:1200px;height:82px;background:var(--white)}
.site-header .brand{left:111px;top:20px;color:var(--ink)}
.site-header .brand .mark-sq{width:30px;height:30px}
.main-nav a{position:absolute;top:31px;font-size:15px;color:#555;text-decoration:none}
.main-nav a.active{color:var(--red);font-weight:500}

/* hero */
.hero{position:absolute;left:0;top:82px;width:1200px;height:967px}
.hero-title{position:absolute;left:100px;top:122px;width:440px;text-align:center;color:var(--white);font-weight:600;font-size:52px;line-height:56px}

/* what we do */
.wwd-photo{left:128px;top:643px;width:277px;height:343px;background:linear-gradient(160deg,#c9b49a,#7a6a5c 55%,#3f5268)}
.wwd-title{left:568px;top:636px;font-size:37px;font-weight:600;color:var(--white);display:flex;align-items:center;gap:16px}
.wwd-text{left:568px;top:710px;width:520px;font-size:16px;line-height:30px;color:#e9e9e9;text-align:justify}

/* section heads */
.section-head{position:absolute;left:0;width:1200px;text-align:center}
.section-head .mark-sq{margin-bottom:10px}
.section-head h2{font-size:37px;font-weight:600;color:var(--ink)}

/* clients */
.client-lead{left:111px;top:1271px;font-size:15px;font-weight:600;color:var(--ink)}
.client-text{left:111px;top:1310px;width:490px;font-size:15px;line-height:30px;text-align:justify}
.client-name{left:113px;top:1446px;font-size:15px;font-weight:600;color:var(--ink)}
.client-photo{left:716px;top:1230px;width:372px;height:278px;background:linear-gradient(150deg,#9fc3d6,#c8c35a 45%,#4e6a3a)}
.testimonial{position:absolute;top:1583px;width:467px;height:247px;background:var(--white);box-shadow:0 4px 22px rgba(0,0,0,.1)}
.testimonial .avatar{position:absolute;left:23px;top:29px;width:102px;height:102px;border-radius:50%;background:linear-gradient(160deg,#b7a79a,#5b4b42);border:1px solid #999}
.testimonial .name{position:absolute;left:149px;top:36px;font-size:18px;font-weight:500;color:var(--ink)}
.testimonial .role{position:absolute;left:149px;top:64px;font-size:14px;color:var(--muted)}
.testimonial .quote{position:absolute;left:150px;top:95px;width:290px;font-size:15px;line-height:30px;color:#333}
.testimonial .qmark{position:absolute;left:28px;top:150px}
.testimonial .corner{position:absolute;right:0;bottom:0;width:20px;height:20px;background:var(--red-soft)}

/* blog */
.blog{position:absolute;left:0;top:1934px;width:1200px;height:691px;background:var(--grey-bg)}
.post{position:absolute;top:196px;width:305px;height:419px;background:var(--white);border:1px solid #d6d6d6}
.post .thumb{height:176px}
.post h3{position:absolute;left:17px;top:27px;width:270px;font-size:17px;font-weight:500;line-height:28px;color:var(--ink)}
.post h3{top:200px}
.post p{position:absolute;left:17px;top:278px;width:270px;font-size:14.5px;line-height:28px;color:#555}
.post .arrow{position:absolute;left:17px;top:371px}

/* contact */
.cta-text{left:0;top:2812px;width:1200px;text-align:center;font-size:15px;line-height:30px;color:#444}
.chat-fab{left:1135px;top:2929px;width:50px;height:50px;border-radius:50%;background:var(--red);box-shadow:0 3px 10px rgba(0,0,0,.25);display:flex;align-items:center;justify-content:center}

/* footer */
.site-footer{position:absolute;left:0;top:2992px;width:1200px;height:198px;background:var(--dark);color:var(--white)}
.site-footer .brand{left:0;width:1200px;justify-content:center;top:42px;color:var(--white)}
.footer-nav{position:absolute;top:114px;left:0;width:1200px;display:flex;justify-content:center;gap:28px;font-size:15px}
.copyright{position:absolute;top:148px;left:0;width:1200px;text-align:center;font-size:15px}
</style>
</head>
<body>

<header class="site-header">
  <div class="brand"><span class="mark-sq"></span>guardwell.ca</div>
  <nav class="main-nav">
    <a class="active" style="left:557px">Home</a>
    <a style="left:638px">About</a>
    <a style="left:718px">Services</a>
    <a style="left:813px">Contact Us</a>
  </nav>
  <a class="btn" style="left:929px;top:21px;width:160px;height:40px">BOOK ONLINE</a>
</header>

<section class="hero">
  <svg class="abs" style="left:0;top:0" width="1200" height="967" viewBox="0 0 1200 967">
    <defs>
      <linearGradient id="heroTone" x1="0" y1="0" x2="1" y2="0.6">
        <stop offset="0" stop-color="#3b3e44"/>
        <stop offset=".45" stop-color="#6d6661"/>
        <stop offset=".75" stop-color="#8a6d52"/>
        <stop offset="1" stop-color="#4d6a58"/>
      </linearGradient>
    </defs>
    <rect x="0" y="0" width="1200" height="967" fill="var(--dark)"/>
    <rect x="0" y="0" width="1200" height="500" fill="url(#heroTone)" role="img" aria-label="Photo: student with a backpack on a waterfront boardwalk in autumn"/>
    <rect x="0" y="0" width="560" height="500" fill="rgba(0,0,0,.35)"/>
    <polygon points="0,370 600,470 1200,370 1200,967 0,967" fill="var(--dark)"/>
    <polygon points="0,370 600,470 1200,370 1200,384 600,484 0,384" fill="var(--red)"/>
    <polygon points="0,384 600,484 1200,384 1200,390 600,490 0,390" fill="var(--white)"/>
  </svg>
  <h1 class="hero-title">Study in Canada<br>as a minor</h1>
  <a class="btn" style="left:239px;top:265px;width:157px;height:41px">LEARN MORE</a>
</section>

<svg class="abs" style="left:0;top:0" width="1200" height="1049">
  <polyline points="318,643 390,610 390,643" fill="none" stroke="var(--red)" stroke-width="2"/>
  <polyline points="128,730 111,738 111,953 128,953" fill="none" stroke="var(--red)" stroke-width="2"/>
</svg>
<div class="abs wwd-photo" role="img" aria-label="Photo: smiling student in a denim jacket at a study table"></div>
<h2 class="abs wwd-title">What We Do? <span class="mark-sq" style="width:20px;height:20px"></span></h2>
<p class="abs wwd-text">We provide the required signed &amp; notarized custodian declaration along with formal supervision service upon the student’s arrival in Canada. According to Citizenship and Immigration Canada (IRCC), minor students can be accepted at a university or college, but they cannot obtain a study permit without the required signed and notarized custodianship form.</p>
<a class="btn" style="left:568px;top:916px;width:160px;height:41px">LEARN MORE</a>

<div class="section-head" style="top:1110px"><span class="mark-sq"></span><h2>Clients Served</h2></div>
<p class="abs client-lead">Sed ut perspiciatis unde omnis iste natus error sit voluptate.</p>
<p class="abs client-text">Lorem ipsum dolor sit amet, consectetur adipiscing elit, sed do eiusmod tempor incididunt ut labore et dolore magna aliqua. Quis ipsum suspendisse ultrices gravida. Risus commodo viverra maecenas accumsan lacus vel facilisis.</p>
<p class="abs client-name">Elise Marchand</p>
<svg class="abs" style="left:690px;top:1240px" width="400" height="300">
  <polyline points="26,16 9,16 9,202 26,202" fill="none" stroke="var(--red)" stroke-width="2"/>
  <polyline points="285,268 381,292 381,268" fill="none" stroke="var(--red)" stroke-width="2"/>
</svg>
<div class="abs client-photo" role="img" aria-label="Photo: two students walking in a city park with a tower behind"></div>

<article class="testimonial" style="left:110px">
  <div class="avatar" role="img" aria-label="Portrait photo of a student"></div>
  <div class="name">Nora Vidal</div><div class="role">Lorem Ipsum set</div>
  <p class="quote">Nemo enim ipsam voluptatem oluptas sit aspernatur aut odit aut fugit, sed quia consequuntur magni dolores eos qui ratione voluptatem sequciunt</p>
  <svg class="qmark" width="84" height="60" viewBox="0 0 84 60"><g fill="none" stroke="var(--red-soft)" stroke-width="2"><path d="M34 4C14 10 4 24 4 40a14 14 0 1 0 26-6"/><path d="M78 4C58 10 48 24 48 40a14 14 0 1 0 26-6"/></g></svg>
  <span class="corner"></span>
</article>
<article class="testimonial" style="left:622px">
  <div class="avatar" role="img" aria-label="Portrait photo of a student"></div>
  <div class="name">Nora Vidal</div><div class="role">Lorem Ipsum set</div>
  <p class="quote">Nemo enim ipsam voluptatem oluptas sit aspernatur aut odit aut fugit, sed quia consequuntur magni dolores eos qui ratione voluptatem sequciunt</p>
  <svg class="qmark" width="84" height="60" viewBox="0 0 84 60"><g fill="none" stroke="var(--red-soft)" stroke-width="2"><path d="M34 4C14 10 4 24 4 40a14 14 0 1 0 26-6"/><path d="M78 4C58 10 48 24 48 40a14 14 0 1 0 26-6"/></g></svg>
  <span class="corner"></span>
</article>

<section class="blog">
  <div class="section-head" style="top:60px"><span class="mark-sq"></span><h2>Latest Blog</h2></div>
  <article class="post" style="left:110px">
    <div class="thumb" role="img" aria-label="Photo: group of students walking in a park" style="background:linear-gradient(160deg,#9bb36a,#5a6b3c)"></div>
    <h3>Lorem ipsum dolor sit amet, consectetur adipiscing.</h3>
    <p>Lorem ipsum dolor sit amet, must consectetur adipiscing. Lorem dol ipsum dolor sit amet.</p>
    <svg class="arrow" width="22" height="16"><path d="M1 8h19M13 2l7 6-7 6" fill="none" stroke="var(--red)" stroke-width="2"/></svg>
  </article>
  <article class="post" style="left:446px">
    <div class="thumb" role="img" aria-label="Photo: student working on a laptop" style="background:linear-gradient(160deg,#cfcac3,#6e6258)"></div>
    <h3>Lorem ipsum dolor sit amet, consectetur adipiscing.</h3>
    <p>Lorem ipsum dolor sit amet, must consectetur adipiscing. Lorem dol ipsum dolor sit amet.</p>
    <svg class="arrow" width="22" height="16"><path d="M1 8h19M13 2l7 6-7 6" fill="none" stroke="var(--red)" stroke-width="2"/></svg>
  </article>
  <article class="post" style="left:781px">
    <div class="thumb" role="img" aria-label="Photo: student in a mask writing in a classroom" style="background:linear-gradient(160deg,#b59a7a,#4a3c33)"></div>
    <h3>Lorem ipsum dolor sit amet, consectetur adipiscing.</h3>
    <p>Lorem ipsum dolor sit amet, must consectetur adipiscing. Lorem dol ipsum dolor sit amet.</p>
    <svg class="arrow" width="22" height="16"><path d="M1 8h19M13 2l7 6-7 6" fill="none" stroke="var(--red)" stroke-width="2"/></svg>
  </article>
</section>

<div class="section-head" style="top:2690px"><span class="mark-sq"></span><h2 style="font-size:36px">Contact us for a free consultation today!</h2></div>
<p class="abs cta-text">Lorem ipsum dolor sit amet, consectetur adipiscing elit, sed do eiusmod tempor incididunt ut labore et dolore magna aliqua.<br>Quis ipsum suspendisse ultrices gravida. Risus commodo viverra maecenas accumsan lacus vel facilisis.</p>
<a class="btn" style="left:520px;top:2914px;width:160px;height:41px">BOOK ONLINE</a>
<div class="abs chat-fab" aria-label="Chat with us">
  <svg width="24" height="24" viewBox="0 0 24 24"><path d="M6.6 10.8a15 15 0 0 0 6.6 6.6l2.2-2.2a1 1 0 0 1 1-.25 11 11 0 0 0 3.6.6 1 1 0 0 1 1 1V20a1 1 0 0 1-1 1A17 17 0 0 1 3 4a1 1 0 0 1 1-1h3.5a1 1 0 0 1 1 1 11 11 0 0 0 .6 3.6 1 1 0 0 1-.25 1z" fill="var(--white)"/></svg>
</div>

<footer class="site-footer">
  <div class="brand"><span class="mark-sq" style="width:30px;height:30px;background:var(--white)"></span>guardwell.ca</div>
  <nav class="footer-nav"><span>Home</span><span>About</span><span>Services</span><span>Contact</span></nav>
  <p class="copyright">2023 guardwell.ca - All Rights Reserved.</p>
</footer>

</body>
</html>
```